GLSW Canberra Pty Ltd

Want something creative and that catches your eye. We are a traffic control companythat offers all aspects of traffic control from planning to roadworks.

Contact Information for Business Card

Dean Vorlick - Director
Ph: 0481 375 206
Email: dean@glsw.com.au
27 Marlow Binks ct Fernbrook ACT 2911

```html
<!DOCTYPE html>
<html lang="en">
<head>
<meta charset="utf-8">
<title>GLSW Canberra – Business Card</title>
<link rel="stylesheet" href="https://fonts.googleapis.com/css2?family=Michroma&display=swap">
<style>
  :root {
    --backdrop: #3a3a3c;
    --card: #262627;
    --card-shade: #1e1e1f;
    --white: #f2f2f2;
    --gold: #b9a23a;
    --gold-light: #e2cf4a;
    --gold-dark: #8f7a22;
    --mark-green: #9ccc7a;
    --tagline-red: #c8392e;
  }
  * { margin: 0; padding: 0; box-sizing: border-box; }
  html, body { width: 1200px; height: 900px; overflow: hidden; }
  body {
    background: var(--backdrop);
    font-family: "Michroma", "Arial", sans-serif;
    position: relative;
  }
  .card {
    position: absolute;
    width: 520px;
    height: 300px;
    background: var(--card);
    overflow: hidden;
    box-shadow: 0 10px 30px rgba(0,0,0,0.45);
  }
  .card--back { left: 90px; top: 130px; }
  .card--front { left: 590px; top: 470px; }
  .card__stripes { position: absolute; inset: 0; width: 520px; height: 300px; }
  .brand {
    position: absolute;
    display: flex;
    align-items: center;
    gap: 10px;
  }
  .brand__dot {
    width: 44px; height: 44px;
    border-radius: 50%;
    background: var(--mark-green);
    flex: none;
  }
  .brand__name { color: var(--white); font-size: 22px; line-height: 1; letter-spacing: 1px; }
  .brand__city { color: var(--white); font-size: 6px; letter-spacing: 1px; margin-top: 4px; }
  .brand__tagline { color: var(--tagline-red); font-size: 6px; margin-top: 3px; }
  .card--back .brand { left: 40px; top: 106px; }
  .card--back .holder { position: absolute; left: 96px; top: 146px; }
  .card--back .holder__name { color: var(--white); font-size: 11px; letter-spacing: 1px; line-height: 1.2; }
  .card--back .holder__role { color: var(--gold); font-size: 8px; letter-spacing: 1px; margin-top: 4px; }
  .card--front .brand { left: 40px; top: 36px; }
  .card--front .holder { position: absolute; left: 40px; top: 120px; }
  .card--front .holder__name { color: var(--white); font-size: 24px; letter-spacing: 1px; line-height: 1.2; }
  .card--front .holder__role { color: var(--gold); font-size: 19px; letter-spacing: 1px; margin-top: 4px; }
  .contact {
    position: absolute; left: 40px; top: 218px;
    list-style: none;
    color: var(--white);
    font-size: 11px;
    line-height: 1.45;
    text-transform: uppercase;
  }
</style>
</head>
<body>
  <svg width="0" height="0" style="position:absolute">
    <defs>
      <linearGradient id="gold-band" x1="0" y1="0" x2="1" y2="1">
        <stop offset="0" stop-color="var(--gold-light)"/>
        <stop offset="0.55" stop-color="var(--gold)"/>
        <stop offset="1" stop-color="var(--gold-dark)"/>
      </linearGradient>
      <g id="hazard-stripes">
        <polygon points="300,0 520,0 520,300 420,300" fill="var(--card-shade)"/>
        <polygon points="395,-14 485,-14 513,14 423,14" fill="url(#gold-band)"/>
        <polygon points="385,32 475,32 503,64 413,64" fill="url(#gold-band)"/>
        <polygon points="395,82 485,82 513,114 423,114" fill="url(#gold-band)"/>
        <polygon points="405,132 495,132 523,164 433,164" fill="url(#gold-band)"/>
        <polygon points="410,182 500,182 528,214 438,214" fill="url(#gold-band)"/>
        <polygon points="420,232 510,232 538,264 448,264" fill="url(#gold-band)"/>
        <polygon points="430,282 520,282 548,314 458,314" fill="url(#gold-band)"/>
      </g>
    </defs>
  </svg>

  <section class="card card--back">
    <svg class="card__stripes" viewBox="0 0 520 300" aria-hidden="true"><use href="#hazard-stripes"/></svg>
    <div class="brand">
      <span class="brand__dot"></span>
      <span class="brand__name">GLSW</span>
    </div>
    <div class="holder">
      <p class="holder__name">DEAN VORLICK</p>
      <p class="holder__role">DIRECTOR</p>
    </div>
  </section>

  <section class="card card--front">
    <svg class="card__stripes" viewBox="0 0 520 300" aria-hidden="true"><use href="#hazard-stripes"/></svg>
    <div class="brand">
      <span class="brand__dot"></span>
      <div>
        <p class="brand__name">GLSW</p>
        <p class="brand__city">CANBERRA</p>
        <p class="brand__tagline">"Always Ahead"</p>
      </div>
    </div>
    <div class="holder">
      <p class="holder__name">DEAN VORLICK</p>
      <p class="holder__role">DIRECTOR</p>
    </div>
    <ul class="contact">
      <li>Ph: 0481 375 206</li>
      <li>Email: dean@glsw.com.au</li>
      <li>27 Marlow Binks ct Fernbrook ACT 2911</li>
    </ul>
  </section>
</body>
</html>
```